Velorine Jewellery Display Card

We are a jewellery manufacturer and need artwork for an A4 size strut card to advertise our new "Crescent Loop Pendant "
In the attached files is a picture of the new pendant and artwork for our trademark "Velorine"
We also need to include the phrase " an expression of love "
as part of the artwork.
The background colour should be predominately white

Target Market(s)

This product has been designed as a gift for Mothers as it has their children names
engraved on the pendant

Industry/Entity Type

Manufacturer

Font styles to use
Serif
Script

Colors
ffffff

Requirements
Must have
• Artwork should be simple and elegant , the predominant look in Australian jewellery stores which is where these display cards will be is white, bright and elegant

```html
<!DOCTYPE html>
<html lang="en">
<head>
<meta charset="utf-8">
<title>Velorine – Crescent Loop Pendant</title>
<link rel="stylesheet" href="https://fonts.googleapis.com/css2?family=Questrial&family=Open+Sans:wght@700&display=swap">
<style>
  :root {
    --card-light: #fafafa;
    --card-mid: #ececec;
    --brand-grey: #a3a3a3;
    --subtitle-grey: #6b6b6b;
    --tagline-grey: #6a6a6a;
    --rule-grey: #b9b9b9;
    --silver-light: #f4f4f4;
    --silver-mid: #cfcfcf;
    --silver-dark: #9c9c9c;
  }
  html, body {
    margin: 0;
    padding: 0;
    width: 1200px;
    height: 907px;
    overflow: hidden;
    background: #ffffff;
  }
  .display-card {
    position: relative;
    width: 1200px;
    height: 907px;
    background: radial-gradient(ellipse at 55% 40%, var(--card-light) 0%, var(--card-mid) 100%);
    overflow: hidden;
  }
  .brand-name {
    position: absolute;
    left: 32px;
    top: 202px;
    margin: 0;
    font-family: "Questrial", sans-serif;
    font-weight: 400;
    font-size: 84px;
    letter-spacing: 3px;
    line-height: 1;
    color: var(--brand-grey);
  }
  .product-name {
    position: absolute;
    left: 54px;
    top: 318px;
    margin: 0;
    font-family: "Questrial", sans-serif;
    font-weight: 400;
    font-size: 45px;
    line-height: 1;
    color: var(--subtitle-grey);
  }
  .tagline {
    position: absolute;
    left: 53px;
    top: 434px;
    margin: 0;
    font-family: "Open Sans", sans-serif;
    font-weight: 700;
    font-size: 41px;
    line-height: 1;
    color: var(--tagline-grey);
  }
  .tagline-rule {
    position: absolute;
    left: 53px;
    top: 508px;
    width: 535px;
    height: 2px;
    background: var(--rule-grey);
  }
  .pendant-visual {
    position: absolute;
    left: 622px;
    top: 130px;
    width: 468px;
    height: 678px;
  }
  .pendant-visual svg {
    display: block;
  }
  .silver-band {
    position: absolute;
    left: 0;
    bottom: 0;
    width: 1200px;
    height: 62px;
    background: linear-gradient(90deg, var(--silver-dark) 0%, var(--silver-light) 45%, var(--silver-mid) 75%, var(--silver-dark) 100%);
    border-top: 3px solid #ffffff;
  }
</style>
</head>
<body>
  <main class="display-card">
    <h1 class="brand-name">VELORINE</h1>
    <p class="product-name">Crescent Loop Pendant</p>
    <p class="tagline">An expression of love</p>
    <div class="tagline-rule"></div>

    <div class="pendant-visual" role="img" aria-label="Product photograph of the silver Crescent Loop Pendant with engraved children's names around a tree-of-life centre, shown large with a smaller view beside it">
      <svg width="468" height="678" viewBox="0 0 468 678">
        <defs>
          <radialGradient id="silverTone" cx="40%" cy="35%" r="70%">
            <stop offset="0%" stop-color="#ffffff"/>
            <stop offset="70%" stop-color="#e2e2e2"/>
            <stop offset="100%" stop-color="#c4c4c4"/>
          </radialGradient>
        </defs>
        <ellipse cx="230" cy="330" rx="228" ry="280" fill="url(#silverTone)"/>
        <ellipse cx="380" cy="548" rx="88" ry="122" fill="url(#silverTone)"/>
      </svg>
    </div>

    <div class="silver-band"></div>
  </main>
</body>
</html>
```